Thermostat Screen Design

We need a screen layout design for a new thermostat we're currently developing. If you're not familiar with thermostats, you can see some examples here - http://smart-climate-units-guide.bestpickdigest.com/

We're after the main page design, with icons, colours etc. It needs to be clean, modern and minimalistic. Attached is all components required on the screen. The screen size is 5 inch (diagnol).

The arrows on the screen showcase what happens when you press a button. For example, when you press MODE once you get OFF, press it twice, HEAT, press it 3 times, COOL, etc. This is just for your reference.

You have complete creative license on how you choose to layout the screen, position the components etc, but we require:

- it must be on a 5 inch screen diagnol
- modern, clean and minimalistic
- includes icons and colours
- Intuitive

Let me know if any questions.

```html
<!DOCTYPE html>
<html lang="en">
<head>
<meta charset="utf-8">
<title>Thermostat Main Screen</title>
<link rel="stylesheet" href="https://fonts.googleapis.com/css2?family=Open+Sans:wght@300;400;600&display=swap">
<style>
  :root {
    --bar-blue: #1a9cec;
    --accent-blue: #1e96ea;
    --panel-bg: #f1efec;
    --sidebar-bg: #e3e2e0;
    --divider: #d9d7d4;
    --text-grey: #6f6f6f;
    --text-mid: #8a8a8a;
    --icon-grey: #9b9b9b;
    --chevron: #d2d0cd;
    --track: #bdbbb8;
    --ring-blue: #1f8fe8;
    --ring-purple: #8b3f8f;
    --ring-red: #e81d1d;
    --white: #ffffff;
  }
  * { box-sizing: border-box; margin: 0; padding: 0; }
  html, body { width: 1200px; height: 680px; overflow: hidden; }
  body {
    font-family: "Open Sans", Arial, sans-serif;
    background: var(--panel-bg);
    position: relative;
    color: var(--text-grey);
  }
  .status-bar {
    position: absolute; left: 0; top: 0; width: 1200px; height: 100px;
    background: var(--bar-blue); color: var(--white);
    display: flex; justify-content: space-between; align-items: center;
    padding: 0 30px 0 22px; font-size: 34px; font-weight: 400; letter-spacing: 0.5px;
  }

  .control-rail {
    position: absolute; left: 0; top: 100px; width: 200px; height: 580px;
    background: var(--sidebar-bg);
  }
  .control { position: absolute; left: 0; width: 200px; }
  .control-mode { top: 0; height: 142px; border-bottom: 3px solid var(--white); }
  .control-fan { top: 145px; height: 143px; border-bottom: 3px solid var(--white); }
  .control-setting { top: 291px; height: 141px; border-bottom: 3px solid var(--white); }
  .control-zone { top: 435px; height: 145px; }

  .control-label, .control-value, .control-icon { position: absolute; left: 0; width: 200px; text-align: center; line-height: 30px; }
  .control-label { top: 3px; font-size: 22px; color: var(--text-mid); }
  .control-icon { display: block; }
  .control-value { top: 100px; font-size: 26px; color: var(--text-mid); }
  .control-value.is-active { color: var(--accent-blue); }
  .control-zone .control-value { top: 58px; font-size: 32px; line-height: 36px; }

  .reading-label { position: absolute; font-size: 38px; color: var(--text-mid); font-weight: 400; line-height: 1.2; }
  .reading-value { position: absolute; font-size: 110px; font-weight: 300; color: var(--text-grey); line-height: 1; }
  .deg { font-size: 70px; vertical-align: top; position: relative; top: -4px; }
  .rule-v { position: absolute; width: 2px; background: var(--divider); }
  .rule-h { position: absolute; height: 2px; background: var(--divider); }
  .humidity { position: absolute; left: 745px; top: 193px; color: var(--text-grey); }
  .humidity-num { font-size: 54px; font-weight: 400; }
  .humidity-unit { position: absolute; left: 66px; top: 4px; font-size: 28px; }
  .humidity-word { position: absolute; left: 66px; top: 38px; font-size: 22px; color: var(--text-mid); }

  .room-label { position: absolute; left: 280px; top: 300px; font-size: 30px; color: var(--text-mid); line-height: 1.2; }
  .setpoint-value { position: absolute; left: 326px; top: 442px; width: 264px; text-align: center;
    font-size: 112px; font-weight: 300; color: var(--text-mid); line-height: 1; }
  .setpoint-value .deg { font-size: 72px; }

  .clock-day { position: absolute; left: 880px; top: 392px; font-size: 30px; color: var(--text-grey); line-height: 1.2; }
  .clock-time { position: absolute; left: 874px; top: 430px; font-size: 88px; letter-spacing: -2px;
    color: var(--accent-blue); font-weight: 400; line-height: 1; }
  .clock-meridiem { position: absolute; left: 1100px; top: 484px; font-size: 26px; color: var(--text-grey); line-height: 1.2; }
  svg.layer { position: absolute; left: 0; top: 0; }
</style>
</head>
<body>
  <header class="status-bar">
    <span class="status-date">SATURDAY, JULY 06, 2014</span>
    <span class="status-zone">ZONE 1</span>
  </header>

  <nav class="control-rail">
    <div class="control control-mode">
      <span class="control-label">Mode</span>
      <svg class="control-icon" style="top:42px;left:72px;width:56px;" width="56" height="56" viewBox="-32 -32 64 64" stroke="var(--accent-blue)" stroke-width="4" fill="none" stroke-linecap="round">
        <line x1="0" y1="-28" x2="0" y2="28"/>
        <line x1="-24" y1="-14" x2="24" y2="14"/>
        <line x1="-24" y1="14" x2="24" y2="-14"/>
        <path d="M-8 -24 L0 -16 L8 -24 M-8 24 L0 16 L8 24"/>
        <path d="M-25 -4 L-14 -8 L-17 -19 M25 4 L14 8 L17 19"/>
        <path d="M-25 4 L-14 8 L-17 19 M25 -4 L14 -8 L17 -19"/>
      </svg>
      <span class="control-value is-active">COOL</span>
    </div>
    <div class="control control-fan">
      <span class="control-label">Fan</span>
      <svg class="control-icon" style="top:42px;left:74px;width:52px;" width="52" height="52" viewBox="-31 -31 62 62" fill="var(--icon-grey)">
        <circle r="5"/>
        <path d="M-3 -6 C-16 -10 -14 -28 -2 -28 C8 -28 10 -16 3 -7 Z"/>
        <path d="M-3 -6 C-16 -10 -14 -28 -2 -28 C8 -28 10 -16 3 -7 Z" transform="rotate(120)"/>
        <path d="M-3 -6 C-16 -10 -14 -28 -2 -28 C8 -28 10 -16 3 -7 Z" transform="rotate(240)"/>
      </svg>
      <span class="control-value">AUTO</span>
    </div>
    <div class="control control-setting">
      <span class="control-label">Setting</span>
      <svg class="control-icon" style="top:40px;left:76px;width:48px;" width="48" height="56" viewBox="0 0 60 66" fill="var(--icon-grey)">
        <path d="M30 2 C34 14 50 22 50 42 C50 56 40 64 30 64 C20 64 10 56 10 42 C10 30 18 24 20 14 C24 20 24 26 26 28 C28 20 30 12 30 2 Z"/>
        <path d="M30 34 C34 42 40 46 38 54 C36 60 24 60 22 54 C20 48 26 44 30 34 Z" fill="var(--sidebar-bg)"/>
      </svg>
      <span class="control-value">HEAT</span>
    </div>
    <div class="control control-zone">
      <span class="control-label">Zone</span>
      <span class="control-value is-active">ZONE 1</span>
    </div>
  </nav>

  <main class="dashboard">
    <span class="reading-label" style="left:280px;top:128px;">Outdoor</span>
    <svg class="layer" width="1200" height="680" aria-hidden="true">
      <g class="weather-icon" fill="none" stroke="var(--text-grey)" stroke-width="4" stroke-linecap="round">
        <circle cx="420" cy="212" r="12"/>
        <line x1="420" y1="186" x2="420" y2="192"/>
        <line x1="440" y1="194" x2="436" y2="198"/>
        <line x1="446" y1="212" x2="440" y2="212"/>
        <line x1="400" y1="194" x2="404" y2="198"/>
        <path d="M378 250 L428 250 C440 250 442 232 430 230 C428 220 412 218 406 226 C396 218 380 224 382 236 C370 238 370 250 378 250 Z" fill="var(--panel-bg)"/>
      </g>
    </svg>
    <div class="reading-value" style="left:480px;top:145px;">48<span class="deg">°</span></div>

    <div class="rule-v" style="left:693px;top:125px;height:145px;"></div>

    <span class="reading-label" style="left:745px;top:128px;">Indoor</span>
    <div class="humidity">
      <span class="humidity-num">25</span>
      <span class="humidity-unit">%</span>
      <span class="humidity-word">Humidity</span>
    </div>
    <div class="reading-value" style="left:955px;top:145px;">48<span class="deg">°</span></div>

    <div class="rule-h" style="left:272px;top:274px;width:855px;"></div>

    <span class="room-label">Room Temperature</span>

    <svg class="layer" width="1200" height="680" aria-hidden="true">
      <defs>
        <linearGradient id="ringGradient" x1="330" y1="0" x2="586" y2="0" gradientUnits="userSpaceOnUse">
          <stop offset="0" stop-color="var(--ring-blue)"/>
          <stop offset="0.25" stop-color="var(--ring-blue)"/>
          <stop offset="0.5" stop-color="var(--ring-purple)"/>
          <stop offset="0.78" stop-color="var(--ring-red)"/>
          <stop offset="1" stop-color="var(--ring-red)"/>
        </linearGradient>
      </defs>
      <path class="setpoint-track" d="M540.3 598 A128 128 0 0 1 375.7 598" fill="none" stroke="var(--track)" stroke-width="3"/>
      <path class="setpoint-ring" d="M375.7 598 A128 128 0 1 1 540.3 598" fill="none" stroke="url(#ringGradient)" stroke-width="16"/>
      <g class="setpoint-adjust" fill="none" stroke="var(--chevron)" stroke-width="4" stroke-linejoin="round">
        <polyline points="645,462 705,402 765,462"/>
        <polyline points="645,530 705,590 765,530"/>
      </g>
    </svg>
    <div class="setpoint-value">18<span class="deg">°</span></div>

    <div class="rule-v" style="left:842px;top:305px;height:307px;"></div>

    <span class="clock-day">Saturday</span>
    <span class="clock-time">11:19</span>
    <span class="clock-meridiem">PM</span>
  </main>
</body>
</html>
```